professional business card design

Business card design. Photos have been uploaded and i am open to the designer choosing which photos to use. Would like the card to be mostyly in a grey scale design with black, whites, silver & grey colours. I have added copy of our flyer as would like on the back side of card our services to be listed. Do not use any bright colurs such as blue red green or yellow. i need to be able to edit the phone number and naem in the final card design submitted.

Target Market(s)

Clients

Industry/Entity Type

earhmovibng and transport

Contact Information for Business Card

Director Name, address, email, phone number and services

Colors

Designer to choose only greyscale colors for use in the design.

Requirements
Should not have
• no yellow, red, blue or green

```html
<!DOCTYPE html>
<html lang="en">
<head>
<meta charset="utf-8">
<title>KRV Pty Ltd – Business Card</title>
<link href="https://fonts.googleapis.com/css2?family=Archivo+Black&family=Arimo:ital,wght@0,400;0,700;1,400&display=swap" rel="stylesheet">
<style>
  :root {
    --page: #d6d6d6;
    --black: #060606;
    --ink: #111111;
    --white: #ffffff;
    --grey-text: #c9c9c9;
    --muted: #9d9d9d;
    --silver: linear-gradient(180deg, #7d7d7d 0%, #d9d9d9 30%, #f4f4f4 50%, #bdbdbd 75%, #8a8a8a 100%);
    --silver-h: linear-gradient(90deg, #8c8c8c 0%, #e6e6e6 35%, #f7f7f7 55%, #b5b5b5 100%);
  }
  * { box-sizing: border-box; margin: 0; padding: 0; }
  html, body { width: 1075px; height: 1200px; overflow: hidden; background: var(--page); }
  body { position: relative; font-family: "Arimo", Arial, sans-serif; }

  .card {
    position: absolute; left: 206px; width: 663px; height: 395px;
    background: var(--black); overflow: hidden;
    box-shadow: 0 2px 5px rgba(0,0,0,.35);
  }
  .card--front { top: 187px; }
  .card--back { top: 637px; }

  /* front */
  .hero {
    position: absolute; left: 0; top: 0; width: 663px; height: 243px;
    background:
      radial-gradient(ellipse 55% 60% at 52% 30%, #3c3c3c 0%, #161616 55%, rgba(0,0,0,0) 100%),
      linear-gradient(180deg, #050505 0%, #0b0b0b 42%, #3a3a3a 62%, #8e8e8e 82%, #b8b8b8 100%);
  }
  .brand-name {
    position: absolute; left: 0; right: 0; top: 26px; text-align: center;
    font-family: "Archivo Black", sans-serif; font-size: 72px; color: #d8d8d8;
    letter-spacing: 4px; line-height: 1;
  }
  .band { position: absolute; background: var(--silver); }
  .band--company { left: 0; top: 243px; width: 663px; height: 38px; }
  .company {
    position: absolute; left: 36px; top: 249px;
    font-family: "Archivo Black", sans-serif; font-size: 25px; letter-spacing: 4px; color: var(--ink); line-height: 1;
  }
  .divider { position: absolute; top: 243px; width: 5px; height: 38px; background: var(--black); }
  .phone {
    position: absolute; font-family: "Archivo Black", sans-serif; font-size: 22px;
    letter-spacing: 4px; color: var(--ink); line-height: 1;
  }
  .phone--front { left: 428px; top: 251px; }
  .icon-phone { position: absolute; width: 24px; height: 24px; }

  .person { position: absolute; left: 35px; top: 296px; color: var(--white); }
  .person__name { font-weight: 700; font-size: 24px; letter-spacing: 1.2px; line-height: 1.05; }
  .person__title { font-size: 18px; color: #e4e4e4; margin-top: 3px; }
  .contact { position: absolute; right: 71px; top: 295px; text-align: right; color: var(--white); font-size: 19px; line-height: 24px; }
  .contact__icon { position: absolute; right: 42px; width: 17px; height: 17px; }

  .band--address { left: 0; top: 357px; width: 663px; height: 38px; background: var(--silver-h); }
  .address { position: absolute; left: 0; right: 0; top: 366px; text-align: center; font-size: 19.5px; color: var(--ink); line-height: 1; }
  .address b { font-weight: 700; }

  /* back */
  .back-visual {
    position: absolute; left: 0; top: 0; width: 342px; height: 395px;
    background:
      radial-gradient(ellipse 60% 40% at 55% 55%, #8a8a8a 0%, #4a4a4a 45%, rgba(20,20,20,0) 100%),
      linear-gradient(180deg, #0a0a0a 0%, #1a1a1a 50%, #0c0c0c 100%);
  }
  .band--phone-icon { left: 0; top: 333px; width: 59px; height: 37px; }
  .band--phone-num { left: 68px; top: 333px; width: 274px; height: 37px; }
  .phone--back { left: 97px; top: 341px; }

  .services { position: absolute; left: 342px; top: 0; width: 321px; height: 395px; background: var(--black); }
  .services__head { position: absolute; left: 0; top: 0; width: 321px; height: 43px; background: var(--silver-h); }
  .services__title { position: absolute; left: 36px; top: 12px; font-weight: 700; font-size: 18.5px; color: var(--ink); letter-spacing: .5px; line-height: 1; }
  .services__list { position: absolute; left: 26px; top: 50px; list-style: none; color: var(--grey-text); font-size: 17px; line-height: 20.5px; }
  .services__list li { position: relative; padding-left: 13px; }
  .services__list li::before { content: ""; position: absolute; left: 0; top: 6px; width: 9px; height: 9px; border-radius: 50%; background: var(--white); }
  .services__note { position: absolute; left: 22px; top: 308px; width: 295px; font-style: italic; font-size: 16.5px; line-height: 20.5px; color: var(--muted); white-space: nowrap; }
  .services__note em { color: var(--white); }
</style>
</head>
<body>

<section class="card card--front">
  <div class="hero" role="img" aria-label="Road train with three tipper trailers on an outback road, dark mesh backdrop"></div>
  <div class="brand-name">KRV</div>

  <div class="band band--company"></div>
  <div class="company">KRV PTY LTD</div>
  <div class="divider" style="left:333px"></div>
  <div class="divider" style="left:396px"></div>
  <svg class="icon-phone" style="left:353px;top:250px" viewBox="0 0 24 24"><path d="M6.6 10.8c1.4 2.8 3.8 5.1 6.6 6.6l2.2-2.2c.3-.3.7-.4 1-.2 1.1.4 2.300.6 3.6.6.6 0 1 .4 1 1V20c0 .6-.4 1-1 1C10.6 21 3 13.4 3 4c0-.6.4-1 1-1h3.5c.6 0 1 .4 1 1 0 1.3.2 2.5.6 3.6.1.3 0 .7-.2 1l-2.3 2.2z" fill="#111"/><path d="M15 3a6 6 0 0 1 6 6M15 6.5A2.5 2.5 0 0 1 17.5 9" stroke="#111" stroke-width="1.6" fill="none"/></svg>
  <div class="phone phone--front">000 123 456</div>

  <div class="person">
    <div class="person__name">MARCUS HALE</div>
    <div class="person__title">Managing Director</div>
  </div>
  <div class="contact">
    <div>email@websitename.com</div>
    <div>www.website.com</div>
  </div>
  <svg class="contact__icon" style="top:300px" viewBox="0 0 16 16"><rect x="1" y="3" width="14" height="10" fill="#fff"/><path d="M1 3l7 6 7-6" stroke="#060606" stroke-width="1.2" fill="none"/></svg>
  <svg class="contact__icon" style="top:324px" viewBox="0 0 16 16"><circle cx="8" cy="8" r="6.5" stroke="#fff" stroke-width="1.4" fill="none"/><ellipse cx="8" cy="8" rx="3" ry="6.5" stroke="#fff" stroke-width="1.2" fill="none"/><path d="M1.5 8h13M2.5 5h11M2.5 11h11" stroke="#fff" stroke-width="1.1"/></svg>

  <div class="band band--address"></div>
  <div class="address"><b>Address:</b> Address Line Goes Here, Adress line and pincode here</div>
</section>

<section class="card card--back">
  <div class="back-visual" role="img" aria-label="Two prime mover trucks with bull bars on a dark mesh backdrop"></div>
  <div class="band band--phone-icon"></div>
  <svg class="icon-phone" style="left:18px;top:340px" viewBox="0 0 24 24"><path d="M6.6 10.8c1.4 2.8 3.8 5.1 6.6 6.6l2.2-2.2c.3-.3.7-.4 1-.2 1.1.4 2.3.6 3.6.6.6 0 1 .4 1 1V20c0 .6-.4 1-1 1C10.6 21 3 13.4 3 4c0-.6.4-1 1-1h3.5c.6 0 1 .4 1 1 0 1.3.2 2.5.6 3.6.1.3 0 .7-.2 1l-2.3 2.2z" fill="#111"/><path d="M15 3a6 6 0 0 1 6 6M15 6.5A2.5 2.5 0 0 1 17.5 9" stroke="#111" stroke-width="1.6" fill="none"/></svg>
  <div class="band band--phone-num"></div>
  <div class="phone phone--back">000 123 456</div>

  <div class="services">
    <div class="services__head"></div>
    <h2 class="services__title">OUR SERVICES</h2>
    <ul class="services__list">
      <li>Over size loads/hot shot loads</li>
      <li>Heavy vehicle recovery services</li>
      <li>Potable water deliveries</li>
      <li>Road building/mainttenance</li>
      <li>Earthworks</li>
      <li>Sand &amp; metal supply &amp;&nbsp; cartage</li>
      <li>Road train tippers</li>
      <li>Road train tankers</li>
      <li>Road train flat tops</li>
      <li>Drop deck trailers</li>
      <li>Mine site accredited<br>Equipment &amp; operators</li>
    </ul>
    <p class="services__note">We offer a large range of services<br>not listed so <em>Call us today for a<br>personalised quote to suit your needs.</em></p>
  </div>
</section>

</body>
</html>
```